Dale Morrikan Plumbing and Heating

Need a card design for a plumbing and heating company that does service and repair, remodels, and plumbing in new construction. Please add following on back side of card; Boilers, Water heaters, Gas lines, Sump pumps, Toilet repairs, Faucet repairs, Pipe thawing, Radiant heating, New construction, Remodels.

Industry/Entity Type

Plumber

Contact Information for Business Card

Was thinking white gloss card with colored logo in middle or black glossy card with silver logo in middle. Just a thought but very open to other designs.

Requirements
Must have
• Need following on front of card;
• P(203) 321-8689
• C(203) 232-9069
• Dale Morrikan 275 Larkwell St West, Stamford, Ct 06214
• service@DrainHearth.example (plumbing in blue, heating in red)
• www.DrainHearth.example (plumbing in blue, heating in red)
• Fully Licensed and Insured
Nice to have
• Elegant design

```html
<!DOCTYPE html>
<html lang="en">
<head>
<meta charset="utf-8">
<title>Dale Morrikan Plumbing and Heating – Business Card</title>
<link rel="stylesheet" href="https://fonts.googleapis.com/css2?family=Source+Sans+3:wght@400;600;700&display=swap">
<style>
  :root {
    --stage-top: #262626;
    --stage-bottom: #080808;
    --card-white: #ffffff;
    --brand-blue: #1f4fa6;
    --accent-blue: #2f8fd8;
    --accent-red: #c8202a;
    --text-gray: #5a5a5a;
    --rule-gray: #b9bcc2;
    --back-top: #5cb6e8;
    --back-bottom: #2d3792;
    --back-text: #ffffff;
  }
  * { margin: 0; padding: 0; box-sizing: border-box; }
  html, body { width: 1200px; height: 900px; overflow: hidden; }
  body {
    position: relative;
    background: linear-gradient(180deg, var(--stage-top) 0%, var(--stage-bottom) 100%);
    font-family: "Source Sans 3", "Myriad Pro", sans-serif;
  }
  .card {
    position: absolute;
    top: 306px;
    height: 271px;
    border-radius: 12px;
    overflow: hidden;
  }
  .card-front { left: 149px; width: 439px; background: var(--card-white); }
  .card-back {
    left: 608px; width: 441px;
    background: linear-gradient(180deg, var(--back-top) 0%, var(--back-bottom) 100%);
    color: var(--back-text);
    text-align: center;
  }
  .front-wordmark {
    position: absolute;
    left: 16px; top: 112px; width: 200px;
    text-align: center;
    color: var(--brand-blue);
    font-weight: 700;
    font-size: 17px;
    line-height: 19px;
    text-transform: uppercase;
    letter-spacing: 0.5px;
  }
  .contact-block { position: absolute; left: 226px; top: 78px; }
  .person-name { color: var(--brand-blue); font-weight: 600; font-size: 16px; line-height: 18px; }
  .person-title { color: var(--text-gray); font-size: 12.5px; line-height: 15px; margin-bottom: 14px; }
  .contact-list { list-style: none; }
  .contact-item {
    display: flex; align-items: center;
    color: var(--text-gray);
    font-size: 13px; line-height: 16px;
  }
  .contact-item svg { width: 9px; height: 9px; margin-right: 7px; margin-left: 2px; fill: var(--brand-blue); }
  .tone-blue { color: var(--accent-blue); }
  .tone-red { color: var(--accent-red); }
  .license-line {
    position: absolute; left: 0; right: 0; top: 232px;
    display: flex; align-items: center;
    color: var(--brand-blue); font-size: 12.5px;
  }
  .license-line::before, .license-line::after {
    content: ""; height: 1px; background: var(--rule-gray);
  }
  .license-line::before { width: 126px; margin-right: 12px; }
  .license-line::after { flex: 1; margin-left: 12px; }
  .back-wordmark {
    margin-top: 96px;
    font-weight: 700;
    font-size: 23px;
    line-height: 25px;
    text-transform: uppercase;
    letter-spacing: 1px;
  }
  .service-list {
    margin-top: 32px;
    font-weight: 600;
    font-size: 13px;
    line-height: 20px;
  }
</style>
</head>
<body>
  <section class="card card-front" aria-label="Card front">
    <div class="front-wordmark">Dale Morrikan<br>Plumbing and Heating</div>
    <div class="contact-block">
      <p class="person-name">Dale Morrikan</p>
      <p class="person-title">Managing Director</p>
      <ul class="contact-list">
        <li class="contact-item">
          <svg viewBox="0 0 10 10" aria-hidden="true"><path d="M3 0h4a1 1 0 0 1 1 1v8a1 1 0 0 1-1 1H3a1 1 0 0 1-1-1V1a1 1 0 0 1 1-1zm0 1.5v6h4v-6z"/></svg>
          (203) 555-0147
        </li>
        <li class="contact-item">
          <svg viewBox="0 0 10 10" aria-hidden="true"><path d="M2.2 0.5l1.8 2-1 1.2c.6 1.3 1.7 2.4 3 3l1.2-1 2 1.8-1 1.8C4.8 9.3 0.7 5.2 0.5 1.5z"/></svg>
          (203) 555-0183
        </li>
        <li class="contact-item">
          <svg viewBox="0 0 10 10" aria-hidden="true"><path d="M0 2h10v6H0zM1 2.5l4 3 4-3v1l-4 3-4-3z" fill-rule="evenodd"/></svg>
          service@<span class="tone-blue">Drain</span><span class="tone-red">Hearth</span>.example
        </li>
        <li class="contact-item">
          <svg viewBox="0 0 10 10" aria-hidden="true"><path d="M5 0a5 5 0 1 0 0 10A5 5 0 0 0 5 0zm0 1c.6.7 1 1.7 1.1 3.5H3.9C4 2.7 4.4 1.7 5 1zM1.1 4.5a4 4 0 0 1 1.8-3C2.5 2.3 2.3 3.4 2.9 4.5zm0 1h1.8c0 1.1.2 2.2.6 3a4 4 0 0 1-2.4-3zm2.8 0h2.2C6 7.3 5.6 8.3 5 9c-.6-.7-1-1.7-1.1-3.5zm3.2 0h1.8a4 4 0 0 1-2.4 3c.4-.8.6-1.9.6-3zm0-1c0-1.1-.2-2.2-.6-3a4 4 0 0 1 2.4 3z"/></svg>
          www.<span class="tone-blue">Drain</span><span class="tone-red">Hearth</span>.example
        </li>
      </ul>
    </div>
    <p class="license-line">Fully Licensed and Insured</p>
  </section>

  <section class="card card-back" aria-label="Card back">
    <div class="back-wordmark">Dale Morrikan<br>Plumbing and Heating</div>
    <p class="service-list">
      Boilers, Water heaters, Gas lines, Sump pumps, Toilet repairs<br>
      Faucet repairs, Pipe thawing, Radiant heating<br>
      New construction, Remodels.
    </p>
  </section>
</body>
</html>
```